Indian Takeaway Menu -

I would like to have double parallel fold A4 sheet menu.
A4 sheet cut in half and attached to the other half to make the sheet 4 small pages long.

Colors
abd036
ffffff

Requirements
Must have
• Please check new attachments - menu size and layout is not correct.
• I would like to add Dark brown colour. A4 sheet folded 4x Menu layout pocket size.
Nice to have
• Dark Brown - Parrot Green and very light Brown

```html
<!DOCTYPE html>
<html lang="en">
<head>
<meta charset="utf-8">
<title>Masala Hearth – Takeaway Menu</title>
<link rel="stylesheet" href="https://fonts.googleapis.com/css2?family=Caveat:wght@600;700&family=Open+Sans:wght@400;600&display=swap">
<style>
  :root{
    --parrot:#abd036;
    --paper-dark:#6f6a3a;
    --paper-mid:#8f8a55;
    --paper-light:#a6a06a;
    --ink:#1f1a0e;
    --brown:#3a2a14;
    --cream:#ece7dc;
    --red:#e0261f;
    --yellow:#f4d21a;
    --white:#ffffff;
  }
  *{box-sizing:border-box;margin:0;padding:0}
  html,body{width:1200px;height:1200px;overflow:hidden;background:var(--white)}
  body{position:relative;font-family:"Open Sans",Arial,sans-serif;color:var(--ink)}
  .menu{position:absolute;left:74px;top:229px;width:1051px;height:742px;display:flex}
  .menu-pages{position:relative;width:698px;height:100%;
    background:radial-gradient(ellipse at 35% 40%,var(--paper-light),var(--paper-mid) 55%,var(--paper-dark) 100%)}
  .column{position:absolute;top:6px}
  .column--left{left:11px;width:320px}
  .column--mid{left:358px;width:320px;top:6px}
  .section-title{font-family:"Caveat",cursive;font-weight:700;font-size:25px;color:var(--parrot);
    text-shadow:1px 1px 2px rgba(40,30,10,.6);line-height:30px;height:30px}
  .dish{position:relative;margin-bottom:2px}
  .dish-head{display:flex;height:17px;align-items:flex-end}
  .dish-name{font-family:"Caveat",cursive;font-weight:600;font-size:18px;line-height:17px;color:var(--ink)}
  .codes{position:absolute;left:222px;top:1px;font-size:10.5px;color:var(--red);letter-spacing:1px}
  .codes .y{color:var(--yellow)}
  .codes .v{color:#3b3520}
  .price{position:absolute;left:280px;top:1px;font-size:11.5px}
  .desc{font-size:11px;line-height:15.2px;color:var(--ink)}
  .gap{height:14px}
  .info-panel{width:353px;height:100%;display:flex;flex-direction:column;background:var(--parrot)}
  .brand{height:110px;display:flex;flex-direction:column;align-items:center;justify-content:flex-end;padding-bottom:8px}
  .brand-name{font-family:"Open Sans",Arial,sans-serif;font-weight:600;font-size:36px;color:var(--ink);line-height:40px}
  .brand-tag{font-size:8.5px;letter-spacing:2px;color:var(--brown);margin-top:2px}
  .contact{height:232px;background:var(--cream);text-align:center;padding-top:14px;color:var(--ink)}
  .phone{font-size:23px;line-height:29px}
  .hours-title{font-size:13.5px;line-height:18px}
  .hours{font-size:17px;line-height:22px}
  .delivery{font-size:17px;line-height:22px;color:var(--red)}
  .cooked{font-size:17px;line-height:22px}
  .web{font-size:26px;color:var(--parrot);font-weight:600;margin-top:12px}
  .photo{height:205px;background:radial-gradient(ellipse at 50% 60%,#a89370,#6e5c3e 70%,#4a3c26)}
  .notice{padding:6px 14px 0;text-align:center;font-size:11.5px;line-height:15px;color:var(--ink)}
  .allergens{margin-top:14px;color:var(--red);font-size:11.5px;line-height:15px;text-align:center;padding:0 14px}
</style>
</head>
<body>
<main class="menu">
  <section class="menu-pages">
    <div class="column column--left">
      <h2 class="section-title">Chicken Dishes</h2>
      <div class="dish"><div class="dish-head"><span class="dish-name">Punjabi Saag</span></div><span class="codes">3 <span class="y">Y</span></span><span class="price">9.95</span><p class="desc">Chicken cooked with spinach, ginger,<br>garlic, fresh cream &amp; temperd with Punjabi tarka.</p></div>
      <div class="dish"><div class="dish-head"><span class="dish-name">Royale Korma</span></div><span class="codes">3 5</span><span class="price">8.95</span><p class="desc">Breast of chicken cooked in a rich creamy sauce with<br>saffron &amp; coconut ,probably most popular among Irish.</p></div>
      <div class="dish"><div class="dish-head"><span class="dish-name">Masala Hearth Chicken Curry</span></div><span class="codes">3 4 5</span><span class="price">8.95</span><p class="desc">Traditional curry cooked with coconut<br>mustard seed ,cashews &amp; curry leaves.</p></div>
      <div class="dish"><div class="dish-head"><span class="dish-name">Chicken Karahi</span></div><span class="price">8.95</span><p class="desc">Boneless chicken prepared in Deg with peppers<br>onion, tomatoes &amp; Indian whole spices.</p></div>
      <div class="dish"><div class="dish-head"><span class="dish-name">Chicken Tikka Masala</span></div><span class="codes">3</span><span class="price">8.95</span><p class="desc">Chicken roasted in clayoven &amp; simmered<br>in smooth creamy tomato sauce with<br>palm crushed fenugreek leaves &amp; jiggery.</p></div>
      <div class="dish"><div class="dish-head"><span class="dish-name">South Indian Garlic Chilli</span></div><span class="price">8.95</span><p class="desc">Chicken cooked in south Indian style &amp;<br>loaded with garlic, ground spices &amp; fresh herbs.</p></div>
      <div class="dish"><div class="dish-head"><span class="dish-name">Chicken Dahiwala</span></div><span class="codes">3</span><span class="price">8.95</span><p class="desc">Amazingly spicy chicken curry cooked<br>with yogurt, green chillies, ginger &amp; herbs.</p></div>
      <div class="dish"><div class="dish-head"><span class="dish-name">Murgh Biryani</span></div><span class="codes">3 5 <span class="y">Y</span></span><span class="price">9.95</span><p class="desc">Perfumed basmati rice with chicken cubes<br>nuts, golden onions &amp; biryani spices, served with sauce.</p></div>
      <h2 class="section-title">Lamb Dishes</h2>
      <div class="dish"><div class="dish-head"><span class="dish-name">Lamb Madras</span></div><span class="price">10.95</span><p class="desc">The popular dish of madras cooked with plum tomato<br>degi chilli ,coconut &amp; finished with hint of lemon juice.</p></div>
      <div class="dish"><div class="dish-head"><span class="dish-name">Palak Gosht</span></div><span class="codes">3 <span class="y">Y</span></span><span class="price">10.95</span><p class="desc">Pan-fried lamb pieces cooked with spinach<br>fresh herbs, ginger &amp; a touch of cream.</p></div>
      <div class="dish"><div class="dish-head"><span class="dish-name">Lamb Roganjosh</span></div><span class="price">10.95</span><p class="desc">Slow cooked tender lamb in kashmiri style<br>with fresh herbs &amp; Himalayan spices.</p></div>
      <div class="dish"><div class="dish-head"><span class="dish-name">Lamb Kohlapuri</span></div><span class="codes">3 4 5</span><span class="price">10.95</span><p class="desc">Lamb dish from South Coast of India<br>flavoured with yoghurt, nuts &amp; coconut.</p></div>
      <div class="dish"><div class="dish-head"><span class="dish-name">Lamb Jalferzi</span></div><span class="codes">3 5</span><span class="price">10.95</span><p class="desc">Lamb tossed with cubes of onions, peppers flavored with<br>crushed coriander seeds &amp; dry fenugreek with hint of<br>cream.</p></div>
    </div>

    <div class="column column--mid">
      <div class="dish"><div class="dish-head"><span class="dish-name">Gosht Biryani</span></div><span class="codes">3 5 <span class="y">Y</span></span><span class="price">11.00</span><p class="desc">Aged rice cooked with tender land brown<br>onions, home made masala &amp; accompanied<br>with curry sauce.</p></div>
      <h2 class="section-title">Prawn Dishes</h2>
      <div class="dish"><div class="dish-head"><span class="dish-name">Prawn Masala</span></div><span class="codes">3</span><span class="price">11.95</span><p class="desc">Prawns in a smooth creamy sauce flavoured<br>with kasoori methi &amp; tandoori spices.</p></div>
      <div class="dish"><div class="dish-head"><span class="dish-name">Prawn Karahi</span></div><span class="price">11.95</span><p class="desc">Prawns cooked with peppers, spring onion<br>caramelised onion, tomatoes &amp; whole spices.</p></div>
      <div class="dish"><div class="dish-head"><span class="dish-name">Goan Prawn Curry</span></div><span class="codes">3 4 5</span><span class="price">11.95</span><p class="desc">Fisherman’s favourite prawn curry aromatic<br>with coconut ,mustard ,nuts ,curry leaves<br>&amp; spices from goa’s costal area.</p></div>
      <div class="dish"><div class="dish-head"><span class="dish-name">Prawn Bhuna</span></div><span class="codes"><span class="v">LF</span></span><span class="price">11.95</span><p class="desc">Prawns cooked in onions &amp; tomato with<br>black pepper to bring together the kick of spices</p></div>
      <div class="gap"></div>
      <div class="dish"><div class="dish-head"><span class="dish-name">Prawn Biryani</span></div><span class="codes">3 6 <span class="y">Y</span></span><span class="price">11.95</span><p class="desc">Pan fried prawn cooked with egg,<br>green peas &amp; onion served with curry sauce.</p></div>
      <h2 class="section-title">Vegetarian Dishes</h2>
      <div class="dish"><div class="dish-head"><span class="dish-name">Shahi Paneer</span></div><span class="codes">3 5</span><span class="price">8.95</span><p class="desc">Indian cheese in semi-dry sauce.</p></div>
      <div class="dish"><div class="dish-head"><span class="dish-name">Subz Maleni Mild</span></div><span class="price">8.95</span><p class="desc">Stir fried vegetables with ground spices.</p></div>
      <div class="dish"><div class="dish-head"><span class="dish-name">Dum Wale Aloo</span></div><span class="codes">3</span><span class="price">8.95</span><p class="desc">Potatoes cooked with ginger, garlic, onions,<br>yoghurt &amp; curry leaves with cumin Flavor.</p></div>
      <div class="dish"><div class="dish-head"><span class="dish-name">Karahi Paneer</span></div><span class="codes">3</span><span class="price">8.95</span><p class="desc">Colorful curry is prepared using homemade<br>Indian cheese (paneer).</p></div>
      <div class="dish"><div class="dish-head"><span class="dish-name">Saag Paneer</span></div><span class="codes">3 <span class="y">Y</span></span><span class="price">8.95</span><p class="desc">Pan fried cottage cheese &amp; spinach with<br>kasoori methi &amp; fresh coriander.</p></div>
      <div class="dish"><div class="dish-head"><span class="dish-name">Sambhar Vegetable Curry</span></div><span class="codes">4 <span class="y">Y</span> <span class="v">V</span></span><span class="price">8.95</span><p class="desc">Vegetable curry cooked with lentils<br>curry leaves, &amp; mustard seeds.</p></div>
      <div class="dish"><div class="dish-head"><span class="dish-name">Vegetable Biryani</span></div><span class="codes">3 5 <span class="y">Y</span> <span class="v">V</span></span><span class="price">8.95</span><p class="desc">Basmati Rice cooked with vegetables,<br>fresh herbs, spices &amp; fried golden onion.<br>Comes with curry sauce.</p></div>
    </div>
  </section>

  <aside class="info-panel">
    <header class="brand">
      <div class="brand-name">Masala Hearth</div>
      <div class="brand-tag">AUTHENTIC INDIAN FOOD AT HOME</div>
    </header>
    <div class="contact">
      <p class="phone">Ph:(0)1 5550147</p>
      <p class="phone">&nbsp;&nbsp;&nbsp;(0)1 5550193</p>
      <p class="hours-title">Opening Hours</p>
      <p class="hours">Sun - Thurs 5.00PM to 10.00PM</p>
      <p class="hours">Fri - Sat 5.00PM-10.30PM</p>
      <p class="delivery">Deliveries From 5.30PM</p>
      <p class="cooked">All our meals are cooked to order.</p>
      <p class="web">www.masalahearth.ie</p>
    </div>
    <div class="photo" role="img" aria-label="Photo of wooden bowls filled with whole spices and coriander seeds"></div>
    <p class="notice">We cook all our meals to order, and each main course is cooked separately, so our pots and pans get used throughout service. Our equipment is washed thoroughly between each preparation, but we cannot guarantee some allergens will not be present. If you are extremely susceptible to nuts for example, please inform us when ordering. No MSG is used in any of our cooking.</p>
    <p class="allergens">1 celery, 2 gluten, 3 dair , 4 mustard, 5 nuts, 6 egg, 7fish,<br>8 soya, 9 penuts, 10 lupin, 11 sulpher dioxide,<br>12 sesame seeds, 13 molluscs, 14 crustanceans</p>
  </aside>
</main>
</body>
</html>
```